Letterhead Design for Law Firm that Specializes in Property Damage Litigation

We are looking for a redesign of our letterhead. Our current letterhead lists all of our current staff members and we'd like to come up with a design that does NOT list all of the staff members so that it does not need to be updated with every newly hired employee. Must be in editable format.

We are a law firm that specializes in property damage, so we need something that is professional, yet modern. The final design should use our existing logo and should use a blue color scheme (alternate colors would be gray, black, and white).

Industry/Entity Type

Legal

Colors
0054AA
0677BA
7BADD7
CADEEF
E8F1F8

```html
<!DOCTYPE html>
<html lang="en">
<head>
<meta charset="utf-8">
<title>Hartwell Corrin &amp; Vance – Letterhead</title>
<link rel="stylesheet" href="https://fonts.googleapis.com/css2?family=Arimo:wght@400;600;700&display=swap">
<style>
  :root {
    --navy: #1d3a6e;
    --slate: #606163;
    --ink: #3b3b3d;
    --rule: #8a8b8d;
    --paper: #ffffff;
    --backdrop: #e6e7e9;
  }
  * { margin: 0; padding: 0; box-sizing: border-box; }
  html, body {
    width: 1013px; height: 1200px; overflow: hidden;
    background: var(--backdrop);
    font-family: "Arimo", Arial, sans-serif;
  }
  .letterhead {
    position: absolute; left: 82px; top: 0;
    width: 849px; height: 1200px;
    background: var(--paper);
  }
  .brand { position: absolute; left: 64px; top: 80px; }
  .brand-name {
    display: flex; align-items: center; gap: 12px;
  }
  .brand-mark {
    width: 34px; height: 34px; background: var(--slate);
  }
  .brand-words {
    color: var(--navy); font-weight: 600; font-size: 22px;
    line-height: 25px; letter-spacing: 1px; text-transform: uppercase;
  }
  .tagline {
    margin-top: 12px; color: var(--slate); font-size: 10.5px;
    letter-spacing: 2.2px; font-weight: 600;
  }
  .divider {
    position: absolute; top: 73px; width: 1px; height: 123px;
    background: var(--rule);
  }
  .divider.first { left: 345px; }
  .divider.second { left: 579px; }
  .office { position: absolute; top: 74px; color: var(--ink); font-size: 13.5px; letter-spacing: 0.4px; }
  .office.philadelphia { left: 377px; }
  .office.new-jersey { left: 606px; top: 72px; }
  .office-title {
    color: var(--navy); font-weight: 700; font-size: 15px;
    letter-spacing: 0.9px; margin-bottom: 5px;
  }
  .office-address { line-height: 20px; }
  .office-contact { margin-top: 8px; line-height: 20px; }
  .contact-line { display: flex; align-items: center; gap: 6px; }
  .icon { width: 11px; height: 11px; fill: var(--navy); flex: none; }
  .footer-rule {
    position: absolute; left: 64px; top: 1111px;
    width: 721px; height: 5px; background: var(--slate);
  }
  .footer-contact {
    position: absolute; left: 0; right: 0; top: 1136px;
    display: flex; justify-content: center; gap: 6px; align-items: center;
    color: var(--navy); font-size: 16.5px; letter-spacing: 0.3px;
  }
  .footer-contact .icon { width: 15px; height: 15px; }
</style>
</head>
<body>
<main class="letterhead">
  <header>
    <div class="brand">
      <div class="brand-name">
        <span class="brand-mark"></span>
        <div class="brand-words">Hartwell<br>Corrin &amp;<br>Vance</div>
      </div>
      <p class="tagline">THE PROPERTY DAMAGE ATTORNEYS</p>
    </div>

    <span class="divider first"></span>
    <section class="office philadelphia">
      <h2 class="office-title">PHILADELPHIA OFFICE</h2>
      <p class="office-address">2480 Larchmont Avenue<br>Suite 840<br>Philadelphia, PA 19107</p>
      <div class="office-contact">
        <p class="contact-line"><svg class="icon" viewBox="0 0 24 24"><path d="M6.6 10.8a15 15 0 0 0 6.6 6.6l2.2-2.2a1 1 0 0 1 1-.25 11.4 11.4 0 0 0 3.6.57 1 1 0 0 1 1 1V20a1 1 0 0 1-1 1A17 17 0 0 1 3 4a1 1 0 0 1 1-1h3.5a1 1 0 0 1 1 1c0 1.25.2 2.45.57 3.57a1 1 0 0 1-.25 1z"/></svg>215.555.0140</p>
        <p class="contact-line"><svg class="icon" viewBox="0 0 24 24"><path d="M6 2h12v6H6zM3 9h18v9h-3v4H6v-4H3zm5 7v4h8v-4z"/></svg>215.555.0172</p>
      </div>
    </section>

    <span class="divider second"></span>
    <section class="office new-jersey">
      <h2 class="office-title">NEW JERSEY OFFICE</h2>
      <p class="office-address">615 Orchard Lane West<br>Suite 310<br>Cherry Hill, NJ 08002</p>
      <div class="office-contact">
        <p class="contact-line"><svg class="icon" viewBox="0 0 24 24"><path d="M6.6 10.8a15 15 0 0 0 6.6 6.6l2.2-2.2a1 1 0 0 1 1-.25 11.4 11.4 0 0 0 3.6.57 1 1 0 0 1 1 1V20a1 1 0 0 1-1 1A17 17 0 0 1 3 4a1 1 0 0 1 1-1h3.5a1 1 0 0 1 1 1c0 1.25.2 2.45.57 3.57a1 1 0 0 1-.25 1z"/></svg>856.555.0193</p>
        <p class="contact-line"><svg class="icon" viewBox="0 0 24 24"><path d="M6 2h12v6H6zM3 9h18v9h-3v4H6v-4H3zm5 7v4h8v-4z"/></svg>215.555.0172</p>
      </div>
    </section>
  </header>

  <footer>
    <span class="footer-rule"></span>
    <p class="footer-contact">
      <svg class="icon" viewBox="0 0 24 24"><path d="M6.6 10.8a15 15 0 0 0 6.6 6.6l2.2-2.2a1 1 0 0 1 1-.25 11.4 11.4 0 0 0 3.6.57 1 1 0 0 1 1 1V20a1 1 0 0 1-1 1A17 17 0 0 1 3 4a1 1 0 0 1 1-1h3.5a1 1 0 0 1 1 1c0 1.25.2 2.45.57 3.57a1 1 0 0 1-.25 1z"/></svg>
      <span>215.555.0140</span>
      <svg class="icon" viewBox="0 0 24 24"><circle cx="12" cy="12" r="9.5" fill="none" stroke="#1d3a6e" stroke-width="2.4"/><path d="M2.5 12h19M12 2.5c3 3 3 16 0 19M12 2.5c-3 3-3 16 0 19" fill="none" stroke="#1d3a6e" stroke-width="1.8"/></svg>
      <span>www.hcvlegal.com</span>
    </p>
  </footer>
</main>
</body>
</html>
```